Tobin's Jewelry Studio Needs a Moving Location Flyer

We need a flyer to inform our customers of our location moving. We will be moving to our city's downtown which is only 1 mile away from our current address. We will be having a moving sale ( Up to 80% off). The sale starts Sept. 8th Our business creates, sells, and repairs fine jewelry. Dimensions are 5"x8"

Target Market(s)

Women ages 25-55

Industry/Entity Type

Jewelry

Colors
85abd2
cfdeed

Requirements
Must have
• Our logo
• Mention of the sale
• Our current address
• 4785 Cresthaven Blvd.
• Dunmore, Ca 94318
• (415)826-3319
Nice to have
• Mention that we're relocating to downtown Dunmore (new location opening Nov. 1st.)

```html
<!DOCTYPE html>
<html lang="en">
<head>
<meta charset="utf-8">
<title>Tobin's Jewelry Studio – Moving Sale</title>
<link rel="stylesheet" href="https://fonts.googleapis.com/css2?family=Tenor+Sans&family=Arimo:wght@400;700&display=swap">
<style>
  :root {
    --page-bg: #e6e6e6;
    --paper: #ffffff;
    --brown: #3b1a10;
    --orange: #f0922c;
    --aqua: #c1e5ea;
    --aqua-line: #9fd2da;
    --rule: #3b1a10;
    --silver-light: #f4f5f7;
    --silver-mid: #dfe2e7;
  }
  * { margin: 0; padding: 0; box-sizing: border-box; }
  html, body { width: 1200px; height: 1200px; overflow: hidden; background: var(--page-bg); }
  .flyer {
    position: absolute; left: 250px; top: 40px;
    width: 700px; height: 1120px;
    background: var(--paper);
    font-family: "Arimo", Arial, sans-serif;
    color: var(--brown);
  }
  .bracelet-photo {
    position: absolute; left: 35px; top: 0; width: 645px; height: 530px;
    border-radius: 0 0 50% 50% / 0 0 60% 60%;
    background: radial-gradient(ellipse at 50% 82%, var(--silver-mid) 0%, var(--silver-light) 30%, var(--paper) 70%);
  }
  .headline {
    position: absolute; left: 0; right: 0; top: 30px;
    text-align: center; font-family: "Tenor Sans", "Optima", sans-serif;
    color: var(--brown); line-height: 1;
  }
  .headline-moving { font-size: 104px; display: block; }
  .headline-sale { font-size: 205px; display: block; margin-top: 2px; letter-spacing: 2px; }
  .discount {
    position: absolute; left: 0; right: 0; top: 420px;
    text-align: center; color: var(--orange);
    font-family: "Tenor Sans", sans-serif; font-size: 54px;
  }
  .discount small { font-size: 31px; margin-right: 6px; }
  .brand-row {
    position: absolute; left: 31px; width: 636px; top: 552px; height: 95px;
    border-top: 1.5px solid var(--rule); border-bottom: 1.5px solid var(--rule);
    display: flex; justify-content: space-around; align-items: center;
    font-size: 22px; color: var(--brown);
  }
  .studio-logo { position: absolute; left: 54px; width: 592px; top: 686px; height: 122px; }
  .studio-logo .rule { position: absolute; top: 60px; height: 3px; width: 100%; background: var(--brown); }
  .studio-logo .mark {
    position: absolute; left: 50%; top: 0; transform: translateX(-50%);
    display: flex; align-items: center; gap: 18px;
    background: var(--paper); padding: 0 18px; height: 122px;
  }
  .studio-logo .dot {
    width: 122px; height: 122px; border-radius: 50%;
    background: var(--aqua);
  }
  .studio-logo .name { font-size: 27px; font-weight: 700; color: var(--brown); }
  .opening { position: absolute; left: 0; right: 0; top: 846px; text-align: center; }
  .opening-label { color: var(--orange); font-size: 34px; display: block; }
  .opening-date { font-size: 56px; display: block; margin-top: 4px; }
  .contact-band {
    position: absolute; left: 0; right: 0; top: 988px; height: 93px;
    background: var(--aqua);
    border-top: 2px solid var(--aqua-line);
    box-shadow: 0 6px 0 -3px var(--paper), 0 8px 0 -3px var(--aqua-line);
    text-align: center; font-size: 24px; color: var(--brown); padding-top: 15px;
  }
  .contact-line { display: flex; justify-content: center; align-items: center; gap: 6px; height: 32px; }
  .contact-line svg { width: 22px; height: 22px; }
  .contact-line .gap { width: 8px; }
</style>
</head>
<body>
  <main class="flyer">
    <div class="bracelet-photo" role="img" aria-label="Silver chain bracelet with a blue evil-eye charm set in pavé stones"></div>

    <h1 class="headline">
      <span class="headline-moving">Moving</span>
      <span class="headline-sale">Sale</span>
    </h1>
    <p class="discount"><small>UP TO</small>80% OFF</p>

    <div class="brand-row">
      <span>Harbor</span>
      <span>lena marlow</span>
      <span>ivo reed</span>
      <span>Vela Corte</span>
      <span>R.T. Gems</span>
    </div>

    <div class="studio-logo">
      <div class="rule"></div>
      <div class="mark">
        <div class="dot"></div>
        <span class="name">tobin's jewelry studio</span>
      </div>
    </div>

    <p class="opening">
      <span class="opening-label">New Location Opening</span>
      <span class="opening-date">November 1st</span>
    </p>

    <footer class="contact-band">
      <div class="contact-line">
        <svg viewBox="0 0 24 24" aria-hidden="true"><circle cx="12" cy="12" r="11" fill="#3b1a10"/><path d="M6 10c0-2 3-3 6-3s6 1 6 3l-2 1-1-2H9l-1 2zM8 12h8l1 5H7z" fill="#fff"/></svg>
        <span>(415) 826-3319</span>
        <span class="gap"></span>
        <svg viewBox="0 0 24 24" aria-hidden="true"><circle cx="12" cy="12" r="10" fill="none" stroke="#3b1a10" stroke-width="2.4"/><ellipse cx="12" cy="12" rx="4" ry="10" fill="none" stroke="#3b1a10" stroke-width="2"/><path d="M2 12h20M4 7h16M4 17h16" stroke="#3b1a10" stroke-width="1.8"/></svg>
        <span>www.tobinsjewelrystudio.com</span>
      </div>
      <div class="contact-line">4785 Cresthaven Blvd. Dunmore, Ca 94318</div>
    </footer>
  </main>
</body>
</html>
```